Business Card Design

we specialise in supply of custom uniforms - teamwear to Schools and sporting clubs, see our website: www.kestrelkitworks.com.au, our main corporate colour is black and white, with small amount of gold/yellow

Industry/Entity Type

Business

Contact Information for Business Card

Kestrel Kit Works
Rowan Petrakis
Ph 03 6219 8805
Mobile 0418 262 740
email: rowan@kestrelkitworks.com.au
www.kestrelkitworks.com.au
like us on facebook

Requirements
Must have
• modern look & feel

```html
<!DOCTYPE html>
<html lang="en">
<head>
<meta charset="utf-8">
<title>Kestrel Kit Works – Business Card</title>
<link rel="stylesheet" href="https://fonts.googleapis.com/css2?family=Archivo+Narrow:wght@700&family=Roboto+Condensed:wght@400&family=Open+Sans:wght@400&display=swap">
<style>
  :root {
    --page: #d9d9d9;
    --card-dark: #0f0f0f;
    --card-mid: #1f1f1f;
    --accent: #f7de2e;
    --ink: #1a1a1a;
    --light: #f2f2f2;
  }
  * { box-sizing: border-box; margin: 0; padding: 0; }
  html, body {
    width: 1200px; height: 900px; overflow: hidden;
    background: var(--page);
  }
  .card {
    position: absolute; left: 75px; top: 150px;
    width: 1050px; height: 600px;
    background: radial-gradient(ellipse at 45% 35%, var(--card-mid) 0%, var(--card-dark) 70%);
    overflow: hidden;
    box-shadow: 0 10px 30px rgba(0,0,0,0.25);
  }
  .brand {
    position: absolute; left: 72px; top: 92px;
    display: flex; align-items: center; gap: 12px;
    font-family: "Archivo Narrow", sans-serif; font-weight: 700;
    font-size: 26px; color: var(--light);
  }
  .brand-dot {
    width: 30px; height: 30px; border-radius: 50%;
    background: var(--light);
  }
  .phones {
    position: absolute; left: 745px; top: 66px;
    list-style: none;
    font-family: "Open Sans", sans-serif; font-size: 17px;
    color: var(--light); letter-spacing: 1px;
  }
  .phones li, .contacts li { display: flex; align-items: center; gap: 14px; }
  .phones li + li { margin-top: 10px; }
  .icon { width: 18px; height: 18px; flex: none; }
  .company-title {
    position: absolute; right: 150px; top: 212px;
    font-family: "Archivo Narrow", sans-serif; font-weight: 700;
    font-size: 48px; color: var(--accent);
    letter-spacing: 0.5px;
  }
  .band {
    position: absolute; left: 0; top: 274px;
    width: 1050px; height: 124px;
  }
  .person-name {
    position: absolute; left: 108px; top: 306px;
    font-family: "Roboto Condensed", sans-serif; font-weight: 400;
    font-size: 40px; color: var(--ink);
  }
  .contacts {
    position: absolute; left: 120px; top: 442px;
    list-style: none;
    font-family: "Open Sans", sans-serif; font-size: 17px;
    color: var(--light); letter-spacing: 0.5px;
  }
  .contacts li + li { margin-top: 16px; }
</style>
</head>
<body>
  <main class="card">
    <div class="brand"><span class="brand-dot"></span>Kestrel Kit Works</div>

    <ul class="phones">
      <li>
        <svg class="icon" viewBox="0 0 18 18"><rect x="5" y="1" width="8" height="16" rx="1.5" fill="none" stroke="var(--accent)" stroke-width="1.8"/><circle cx="9" cy="14" r="1" fill="var(--accent)"/></svg>
        0418 262 740
      </li>
      <li>
        <svg class="icon" viewBox="0 0 18 18"><path d="M4 2 L7 2 L8 6 L6 7.5 Q7.5 10.5 10.5 12 L12 10 L16 11 L16 14 Q16 16 14 16 Q3 15 2 4 Q2 2 4 2 Z" fill="var(--accent)"/></svg>
        03 6219 8805
      </li>
    </ul>

    <h1 class="company-title">Kestrel Kit Works</h1>

    <svg class="band" viewBox="0 0 1050 124" aria-hidden="true">
      <polygon points="0,0 445,0 420,124 0,124" fill="var(--accent)"/>
      <g fill="var(--accent)">
        <polygon points="470,0 490,0 465,124 445,124"/>
        <polygon points="510,0 530,0 505,124 485,124"/>
        <polygon points="550,0 570,0 545,124 525,124"/>
        <polygon points="590,0 610,0 585,124 565,124"/>
        <polygon points="630,0 650,0 625,124 605,124"/>
        <polygon points="670,0 690,0 665,124 645,124"/>
        <polygon points="710,0 730,0 705,124 685,124"/>
        <polygon points="750,0 770,0 745,124 725,124"/>
        <polygon points="790,0 810,0 785,124 765,124"/>
        <polygon points="830,0 850,0 825,124 805,124"/>
        <polygon points="870,0 890,0 865,124 845,124"/>
      </g>
      <polygon points="910,0 1050,0 1050,124 885,124" fill="var(--accent)"/>
    </svg>

    <p class="person-name">Rowan Petrakis</p>

    <ul class="contacts">
      <li>
        <svg class="icon" viewBox="0 0 18 18"><circle cx="9" cy="9" r="7.5" fill="var(--accent)"/><path d="M2 9 H16 M9 1.5 Q5 9 9 16.5 M9 1.5 Q13 9 9 16.5" stroke="var(--card-dark)" stroke-width="1.2" fill="none"/></svg>
        www.kestrelkitworks.com.au
      </li>
      <li>
        <svg class="icon" viewBox="0 0 18 18"><rect x="1" y="1" width="16" height="16" rx="2" fill="var(--accent)"/></svg>
        / kestrelkitworks
      </li>
      <li>
        <svg class="icon" viewBox="0 0 18 18"><circle cx="9" cy="9" r="8" fill="var(--accent)"/><rect x="4.5" y="5.5" width="9" height="7" fill="none" stroke="var(--card-dark)" stroke-width="1.2"/><path d="M4.5 5.5 L9 9.5 L13.5 5.5" fill="none" stroke="var(--card-dark)" stroke-width="1.2"/></svg>
        rowan@kestrelkitworks.com.au
      </li>
    </ul>
  </main>
</body>
</html>
```